Business Card, Stationary with Shark Logo for Personal Injury Lawyer

I need business cards and stationery with a shark logo for my Personal Injury Law Practice. Has to have this written on it:
Martin K. Hollis
Injury Lawyer
The Corvell Building
718 Tandy Street
Providence, Rhode Island 02908
401-627-4193
Martinhollis.com

Contact Information for Business Card

Martin K. Hollis, Injury Lawyer, address, 401-627-4193, martinhollis.com

```html
<!DOCTYPE html>
<html lang="en">
<head>
<meta charset="utf-8">
<title>Martin K. Hollis – Business Card</title>
<link rel="stylesheet" href="https://fonts.googleapis.com/css2?family=Barlow:wght@400&display=swap">
<style>
  :root {
    --page: #fefefe;
    --navy: #272a60;
    --blue-deep: #1e7fc8;
    --blue-mid: #18a8e0;
    --blue-bright: #14c2ec;
    --blue-soft: #44c4e2;
  }
  * { margin: 0; padding: 0; box-sizing: border-box; }
  html, body {
    width: 1200px; height: 1000px; overflow: hidden;
    background: var(--page);
  }
  .card {
    position: absolute; left: 181px; top: 261px;
    width: 838px; height: 478px;
    background:
      radial-gradient(ellipse 420px 300px at 800px 90px, var(--blue-soft), transparent 70%),
      radial-gradient(ellipse 360px 260px at 470px 170px, var(--blue-bright), transparent 75%),
      radial-gradient(ellipse 380px 300px at 60px 420px, var(--blue-deep), transparent 80%),
      linear-gradient(120deg, var(--blue-deep) 0%, var(--blue-mid) 45%, var(--blue-bright) 75%, var(--blue-mid) 100%);
    font-family: "Barlow", "DIN Alternate", Arial, sans-serif;
    color: var(--navy);
  }
  .brand {
    position: absolute; left: 43px; top: 152px; width: 342px;
    text-align: center;
  }
  .brand-name {
    font-size: 44px; font-weight: 400; line-height: 1.15;
  }
  .brand-role {
    font-size: 44px; font-weight: 400; line-height: 1.15;
  }
  .divider {
    position: absolute; left: 419px; top: 127px;
    width: 2px; height: 216px; background: var(--navy);
  }
  .contact {
    position: absolute; left: 444px; top: 122px;
    list-style: none;
    font-size: 26px; line-height: 32px; letter-spacing: 0.9px;
  }
  .contact li { position: relative; padding-left: 39px; }
  .contact .icon {
    position: absolute; left: 0; top: 6px;
    width: 22px; height: 22px; fill: var(--navy);
  }
</style>
</head>
<body>
  <section class="card">
    <div class="brand">
      <div class="brand-name">Martin K. Hollis</div>
      <div class="brand-role">Injury Lawyer</div>
    </div>

    <div class="divider"></div>

    <ul class="contact">
      <li>
        <svg class="icon" viewBox="0 0 24 24" aria-hidden="true"><path d="M12 1a8 8 0 0 0-8 8c0 6 8 14 8 14s8-8 8-14a8 8 0 0 0-8-8zm0 11a3 3 0 1 1 0-6 3 3 0 0 1 0 6z"/></svg>
        The Corvell Building<br>718 Tandy Street<br>Providence,<br>Rhode Island 02908
      </li>
      <li>
        <svg class="icon" viewBox="0 0 24 24" aria-hidden="true"><path d="M6.6 10.8a15 15 0 0 0 6.6 6.6l2.2-2.2a1 1 0 0 1 1-.25 11 11 0 0 0 3.6.6 1 1 0 0 1 1 1V20a1 1 0 0 1-1 1A17 17 0 0 1 3 4a1 1 0 0 1 1-1h3.5a1 1 0 0 1 1 1 11 11 0 0 0 .6 3.6 1 1 0 0 1-.25 1z"/><path d="M14 2a8 8 0 0 1 8 8h-2a6 6 0 0 0-6-6zm0 4a4 4 0 0 1 4 4h-2a2 2 0 0 0-2-2z"/></svg>
        401-627-4193
      </li>
      <li>
        <svg class="icon" viewBox="0 0 24 24" aria-hidden="true"><path d="M2 5h20v14H2z" fill="none"/><path d="M2 5h20v2l-10 6L2 7zM2 9l10 6 10-6v10H2z"/></svg>
        Martin@martinhollis.com
      </li>
      <li>
        <svg class="icon" viewBox="0 0 24 24" aria-hidden="true"><circle cx="12" cy="12" r="10"/><path d="M2 12h20M12 2v20M4 7h16M4 17h16M12 2c-4 5-4 15 0 20M12 2c4 5 4 15 0 20" stroke="#27b6e6" stroke-width="1.3" fill="none"/></svg>
        Martinhollis.com
      </li>
    </ul>
  </section>
</body>
</html>
```